International Education App needs UI Design

My current app is being upgraded and totally rebranded. This app is aimed to become No1. communication app for schools worldwide. Aimed at parents and high school students it will have events, assessments, messages, newsletters, notes, policies, contact us plus much more.
It will need to be much engaging and professional than all other apps on the market. You can see them attached to compare as well as the app logo to tie in the design. You can also see my current app and why needs an upgrade.
There will need to be design for each screen.
Needs a slick and professional finish with Tranvelo Blue as the base colour.
The app is called ClassNook
You will also find a file attached which shows functionality which will help design screens.

Target Market(s)

Parents, High Schools Students

Industry/Entity Type

Education

Font styles to use
Sans Serif

Colors
0355a3

Requirements
Must have
• Sleek, modern, professional and better than examples provided.
• I need a splash screen, home screen and each of the other screens designed.

```html
<!DOCTYPE html>
<html lang="en">
<head>
<meta charset="utf-8">
<title>ClassNook – Home</title>
<link rel="stylesheet" href="https://fonts.googleapis.com/css2?family=Roboto:wght@400;500&display=swap">
<style>
  :root{
    --brand-blue:#0a55ad;
    --brand-blue-deep:#074894;
    --body-bg:#262626;
    --tile-bg:#3a3a3a;
    --tile-active:#5a5a5a;
    --tile-edge:#4a4a4a;
    --icon-disc:#2c2c2c;
    --icon-ring:#9a9a9a;
    --text-light:#ffffff;
    --text-muted:#b9b9b9;
    --tab-bg:#1c1c1c;
    --tab-active:#1f8fd6;
    --tab-star:#5fd35a;
  }
  *{box-sizing:border-box;margin:0;padding:0}
  html,body{width:1200px;height:2352px;overflow:hidden;background:var(--body-bg)}
  body{font-family:"Roboto",Helvetica,Arial,sans-serif;color:var(--text-light);position:relative}

  .status-bar{position:absolute;top:0;left:0;width:1200px;height:60px;background:var(--brand-blue-deep);
    display:flex;align-items:center;justify-content:space-between;padding:0 28px;font-size:34px}
  .status-left,.status-right{display:flex;align-items:center;gap:14px;width:340px}
  .status-right{justify-content:flex-end}
  .signal{display:flex;gap:6px}
  .signal span{width:14px;height:14px;border-radius:50%;background:var(--text-light)}
  .signal span.dim{background:none;border:2px solid var(--text-light)}
  .status-time{font-weight:500}
  .battery{width:66px;height:30px;border:3px solid var(--text-light);border-radius:5px;padding:3px;position:relative}
  .battery::after{content:"";position:absolute;right:-9px;top:8px;width:5px;height:10px;background:var(--text-light);border-radius:0 2px 2px 0}
  .battery i{display:block;height:100%;background:var(--text-light);border-radius:2px}

  .app-header{position:absolute;top:60px;left:0;width:1200px;height:140px;background:var(--brand-blue);
    display:flex;align-items:center;justify-content:center}
  .app-title{font-size:46px;font-weight:400}
  .menu-button{position:absolute;right:44px;top:44px;width:70px;height:52px;display:flex;flex-direction:column;justify-content:space-between}
  .menu-button span{height:7px;background:var(--text-light);border-radius:2px}

  .module-grid{position:absolute;top:228px;left:40px;width:1120px;display:grid;
    grid-template-columns:repeat(3,364px);grid-auto-rows:360px;gap:14px}
  .module-tile{background:var(--tile-bg);border:2px solid var(--tile-edge);display:flex;flex-direction:column;
    align-items:center;justify-content:center;gap:26px}
  .module-tile.is-active{background:var(--tile-active)}
  .module-tile.is-last{grid-column:2}
  .module-icon{position:relative;width:180px;height:180px;border-radius:50%;background:var(--icon-disc);
    border:8px solid var(--icon-ring);display:flex;align-items:center;justify-content:center}
  .module-icon svg{width:104px;height:104px}
  .count-badge{position:absolute;right:-4px;bottom:-2px;min-width:52px;height:52px;padding:0 8px;border-radius:26px;
    background:var(--icon-disc);border:4px solid var(--text-light);font-size:24px;font-weight:500;
    display:flex;align-items:center;justify-content:center}
  .module-label{font-size:44px}

  .tab-bar{position:absolute;left:0;bottom:0;width:1200px;height:196px;background:var(--tab-bg);display:flex}
  .tab-item{flex:1;display:flex;flex-direction:column;align-items:center;justify-content:center;gap:14px;
    color:var(--text-muted);font-size:30px}
  .tab-item svg{width:76px;height:76px}
  .tab-item.is-current{background:var(--tab-active);color:var(--tab-star)}
</style>
</head>
<body>
  <div class="status-bar">
    <div class="status-left">
      <div class="signal"><span></span><span></span><span></span><span class="dim"></span><span class="dim"></span></div>
      <span>CORVO</span>
      <svg width="36" height="28" viewBox="0 0 36 28"><path d="M2 10a24 24 0 0 1 32 0M8 16a15 15 0 0 1 20 0M14 22a6 6 0 0 1 8 0" stroke="#fff" stroke-width="4" fill="none" stroke-linecap="round"/></svg>
    </div>
    <div class="status-time">4:21 PM</div>
    <div class="status-right">
      <svg width="20" height="32" viewBox="0 0 20 32"><path d="M3 9l14 14-7 7V2l7 7L3 23" stroke="#fff" stroke-width="3" fill="none"/></svg>
      <span>100%</span>
      <div class="battery"><i></i></div>
    </div>
  </div>

  <header class="app-header">
    <h1 class="app-title">Home</h1>
    <div class="menu-button"><span></span><span></span><span></span></div>
  </header>

  <main class="module-grid">
    <div class="module-tile">
      <div class="module-icon">
        <svg viewBox="0 0 100 100" fill="#fff"><circle cx="50" cy="32" r="18"/><path d="M32 30l18-10 18 10-18 8z"/><path d="M16 92c0-22 15-36 34-36s34 14 34 36z"/></svg>
        <span class="count-badge">25</span>
      </div>
      <span class="module-label">Students</span>
    </div>
    <div class="module-tile">
      <div class="module-icon">
        <svg viewBox="0 0 100 100" fill="none" stroke="#fff" stroke-width="5"><rect x="10" y="24" width="56" height="56" rx="4"/><line x1="10" y1="38" x2="66" y2="38"/><text x="20" y="70" fill="#fff" stroke="none" font-size="26" font-family="Roboto,sans-serif">12</text><circle cx="70" cy="30" r="20" fill="#2c2c2c"/><path d="M70 20v11l8 5"/></svg>
        <span class="count-badge">2</span>
      </div>
      <span class="module-label">Events</span>
    </div>
    <div class="module-tile">
      <div class="module-icon">
        <svg viewBox="0 0 100 100" fill="#fff"><path d="M10 24h80v52H10z"/><path d="M10 24l40 32 40-32" stroke="#2c2c2c" stroke-width="5" fill="none"/></svg>
        <span class="count-badge">1</span>
      </div>
      <span class="module-label">Messages</span>
    </div>
    <div class="module-tile is-active">
      <div class="module-icon">
        <svg viewBox="0 0 100 100" fill="none" stroke="#fff" stroke-width="5"><rect x="18" y="16" width="66" height="68" rx="4"/><path d="M18 30H10v48a6 6 0 0 0 12 0"/><rect x="28" y="28" width="20" height="18" fill="#fff"/><line x1="54" y1="30" x2="74" y2="30"/><line x1="54" y1="42" x2="74" y2="42"/><line x1="28" y1="56" x2="74" y2="56"/><line x1="28" y1="68" x2="74" y2="68"/></svg>
        <span class="count-badge">6</span>
      </div>
      <span class="module-label">Newsletters</span>
    </div>
    <div class="module-tile">
      <div class="module-icon">
        <svg viewBox="0 0 100 100" fill="none" stroke="#fff" stroke-width="5"><rect x="18" y="14" width="56" height="74" rx="4"/><line x1="28" y1="32" x2="62" y2="32"/><line x1="28" y1="46" x2="62" y2="46"/><line x1="28" y1="60" x2="50" y2="60"/><path d="M84 30L58 72l-6 10 10-6 26-42z" fill="#fff"/></svg>
        <span class="count-badge">4</span>
      </div>
      <span class="module-label">Notes</span>
    </div>
    <div class="module-tile">
      <div class="module-icon">
        <svg viewBox="0 0 100 100" fill="#fff"><path d="M28 64a18 18 0 0 1-4-34 22 22 0 0 1 40-6 18 18 0 0 1 8 40z"/><rect x="28" y="68" width="44" height="18" rx="3"/></svg>
        <span class="count-badge">2</span>
      </div>
      <span class="module-label">Canteen</span>
    </div>
    <div class="module-tile">
      <div class="module-icon">
        <svg viewBox="0 0 100 100" fill="none" stroke="#fff" stroke-width="5"><rect x="14" y="20" width="72" height="66" rx="5"/><line x1="14" y1="36" x2="86" y2="36"/><line x1="32" y1="12" x2="32" y2="26"/><line x1="68" y1="12" x2="68" y2="26"/><g fill="#fff" stroke="none"><rect x="24" y="46" width="10" height="10"/><rect x="45" y="46" width="10" height="10"/><rect x="66" y="46" width="10" height="10"/><rect x="24" y="64" width="10" height="10"/><rect x="45" y="64" width="10" height="10"/></g></svg>
        <span class="count-badge">5</span>
      </div>
      <span class="module-label">Calendar</span>
    </div>
    <div class="module-tile">
      <div class="module-icon">
        <svg viewBox="0 0 100 100" fill="#fff"><rect x="16" y="18" width="68" height="18" rx="3"/><rect x="12" y="42" width="76" height="18" rx="3"/><rect x="18" y="66" width="66" height="18" rx="3"/><g stroke="#2c2c2c" stroke-width="3"><line x1="70" y1="18" x2="70" y2="36"/><line x1="24" y1="42" x2="24" y2="60"/><line x1="72" y1="66" x2="72" y2="84"/></g></svg>
        <span class="count-badge">11</span>
      </div>
      <span class="module-label">Books</span>
    </div>
    <div class="module-tile">
      <div class="module-icon">
        <svg viewBox="0 0 100 100" fill="#fff"><line x1="30" y1="50" x2="70" y2="26" stroke="#fff" stroke-width="5"/><line x1="30" y1="50" x2="70" y2="74" stroke="#fff" stroke-width="5"/><circle cx="28" cy="50" r="12"/><circle cx="72" cy="24" r="12"/><circle cx="72" cy="76" r="12"/></svg>
        <span class="count-badge">0</span>
      </div>
      <span class="module-label">Share</span>
    </div>
    <div class="module-tile is-last">
      <div class="module-icon">
        <svg viewBox="0 0 100 100" fill="none" stroke="#fff" stroke-width="5"><circle cx="50" cy="50" r="38"/><path d="M36 28l8 12-6 6c3 7 9 13 16 16l6-6 12 8-6 8c-18-2-34-18-36-36z" fill="#fff"/></svg>
        <span class="count-badge">53</span>
      </div>
      <span class="module-label">Contacts</span>
    </div>
  </main>

  <nav class="tab-bar">
    <div class="tab-item is-current">
      <svg viewBox="0 0 100 100" fill="none" stroke="currentColor" stroke-width="5" stroke-linejoin="round"><path d="M50 8l12 28 30 2-23 20 7 30-26-16-26 16 7-30L8 38l30-2z"/></svg>
      <span>Featured</span>
    </div>
    <div class="tab-item">
      <svg viewBox="0 0 100 100" fill="none" stroke="currentColor" stroke-width="5"><rect x="20" y="14" width="60" height="76" rx="4"/><rect x="38" y="8" width="24" height="12" rx="3"/><line x1="32" y1="38" x2="68" y2="38"/><line x1="32" y1="54" x2="68" y2="54"/><line x1="32" y1="70" x2="56" y2="70"/></svg>
      <span>Top Charts</span>
    </div>
    <div class="tab-item">
      <svg viewBox="0 0 100 100" fill="none" stroke="currentColor" stroke-width="5"><path d="M50 70C36 52 28 42 28 32a22 22 0 0 1 44 0c0 10-8 20-22 38z"/><circle cx="50" cy="32" r="8"/><ellipse cx="50" cy="80" rx="30" ry="10"/></svg>
      <span>Near me</span>
    </div>
    <div class="tab-item">
      <svg viewBox="0 0 100 100" fill="none" stroke="currentColor" stroke-width="6" stroke-linecap="round"><circle cx="42" cy="42" r="26"/><line x1="62" y1="62" x2="88" y2="88"/></svg>
      <span>Search</span>
    </div>
    <div class="tab-item">
      <svg viewBox="0 0 100 100" fill="none" stroke="currentColor" stroke-width="5"><path d="M14 50v36h72V50"/><path d="M50 12v52M34 48l16 16 16-16"/></svg>
      <span>Updates</span>
    </div>
  </nav>
</body>
</html>
```